Business Card, A4 Letter Head and DL Envelope for Vantrelle

We are looking for a design for our Business Card, A4 Letter Head and DL Envelope.

Vantrelle is a distributor of promotional products. We specialize in a range of branded promotional products, these include pens, polo shirts, key rings, drink bottles, uniforms and bags to name a few. We are experts in marketing and assist companies in choosing the right promotional product for their needs. We will predominately be an online business where customers visit our website and browse our range of promotional products and branding options.

Our colours are black, red, white and grey.

Files must be supplied in eps, pdf and ai format.

Please display the following information:
Corbin Hale
Account Manager
Suite xxx, 214 Dawlish Parade Melbourne, Victoria 3000
Phone +61 3 5550 1827
Mobile +61 455 501 936
sales@vantrelle.com.au
www.vantrelle.com.au

```html
<!DOCTYPE html>
<html lang="en">
<head>
<meta charset="utf-8">
<title>Vantrelle Business Card</title>
<link rel="stylesheet" href="https://fonts.googleapis.com/css2?family=PT+Sans+Narrow:wght@400;700&display=swap">
<style>
  :root {
    --stage-dark: #050505;
    --stage-mid: #2a2a2a;
    --brand-red: #ff0000;
    --deep-red: #5a0000;
    --paper: #ffffff;
    --ink: #111111;
    --wordmark: #3a3a3a;
    --text-light: #ffffff;
    --text-soft: #f2dada;
  }
  * { margin: 0; padding: 0; box-sizing: border-box; }
  html, body { width: 1200px; height: 1000px; overflow: hidden; }
  body {
    background: radial-gradient(ellipse at 50% 50%, var(--stage-mid) 0%, var(--stage-dark) 70%);
    font-family: "PT Sans Narrow", "Arial Narrow", sans-serif;
    position: relative;
  }
  .card {
    position: absolute;
    left: 276px;
    width: 649px;
    height: 378px;
    box-shadow: 18px 22px 30px rgba(0,0,0,0.75);
    overflow: hidden;
  }
  .card--front { top: 100px; }
  .card--back { top: 527px; }
  .card__art { position: absolute; inset: 0; width: 100%; height: 100%; }
  .brand {
    position: absolute;
    display: flex;
    flex-direction: column;
    align-items: center;
    gap: 22px;
  }
  .brand__dot {
    width: 84px; height: 84px; border-radius: 50%;
    background: var(--brand-red);
  }
  .brand__name {
    font-weight: 700;
    font-size: 40px;
    letter-spacing: 1px;
    text-transform: uppercase;
    color: var(--wordmark);
    line-height: 1;
  }
  .card--front .brand { left: 0; width: 649px; top: 112px; }
  .card--back .brand { left: 57px; width: 300px; top: 97px; }
  .person {
    position: absolute;
    right: 22px; top: 17px;
    text-align: right;
    color: var(--text-light);
  }
  .person__name { font-weight: 700; font-size: 17px; line-height: 20px; }
  .person__role { font-size: 12.5px; line-height: 14px; }
  .contact {
    position: absolute;
    left: 429px; top: 245px;
    width: 198px;
    list-style: none;
  }
  .contact__row {
    position: relative;
    height: 40px;
    border-top: 2px solid var(--brand-red);
    padding: 3px 34px 0 0;
    color: var(--text-light);
    font-size: 12.5px;
    line-height: 16px;
    margin-bottom: 0;
  }
  .contact__icon {
    position: absolute;
    right: 0; top: -2px;
    width: 30px; height: 31px;
    background: var(--brand-red);
    display: flex; align-items: center; justify-content: center;
  }
  .contact__icon svg { width: 20px; height: 20px; }
</style>
</head>
<body>

<section class="card card--front">
  <svg class="card__art" viewBox="0 0 649 378" aria-hidden="true">
    <defs>
      <radialGradient id="front-left-glow" cx="110" cy="190" r="240" gradientUnits="userSpaceOnUse">
        <stop offset="0" stop-color="#ff0000"/>
        <stop offset="1" stop-color="#4a0000"/>
      </radialGradient>
      <radialGradient id="front-right-glow" cx="560" cy="190" r="230" gradientUnits="userSpaceOnUse">
        <stop offset="0" stop-color="#ff0000"/>
        <stop offset="1" stop-color="#4a0000"/>
      </radialGradient>
    </defs>
    <rect x="0" y="0" width="325" height="378" fill="url(#front-left-glow)"/>
    <rect x="325" y="0" width="324" height="378" fill="url(#front-right-glow)"/>
    <polygon points="111,0 536,0 562,190 536,378 111,378 87,190" fill="#ffffff"/>
    <polyline points="122,0 98,190 122,378" fill="none" stroke="#111" stroke-width="2.5"/>
    <polyline points="525,0 551,190 525,378" fill="none" stroke="#111" stroke-width="2.5"/>
  </svg>
  <div class="brand">
    <span class="brand__dot"></span>
    <span class="brand__name">Vantrelle</span>
  </div>
</section>

<section class="card card--back">
  <svg class="card__art" viewBox="0 0 649 378" aria-hidden="true">
    <defs>
      <radialGradient id="back-glow" cx="440" cy="90" r="300" gradientUnits="userSpaceOnUse">
        <stop offset="0" stop-color="#ff0000"/>
        <stop offset="0.55" stop-color="#a00000"/>
        <stop offset="1" stop-color="#3e0000"/>
      </radialGradient>
    </defs>
    <rect x="0" y="0" width="649" height="378" fill="#ffffff"/>
    <polygon points="403,0 649,0 649,378 403,378 425,190" fill="url(#back-glow)"/>
    <polyline points="392,0 414,190 392,378" fill="none" stroke="#111" stroke-width="2.5"/>
  </svg>

  <div class="brand">
    <span class="brand__dot"></span>
    <span class="brand__name">Vantrelle</span>
  </div>

  <div class="person">
    <p class="person__name">Corbin Hale</p>
    <p class="person__role">Account Manager</p>
  </div>

  <ul class="contact">
    <li class="contact__row">
      Phone +61 3 5550 1827<br>Mobile +61 455 501 936
      <span class="contact__icon">
        <svg viewBox="0 0 20 20" aria-hidden="true">
          <path d="M2 8 C2 3 18 3 18 8 L14 9 L13 7 C11 6 9 6 7 7 L6 9 Z" fill="#fff"/>
          <path d="M5 10 L15 10 L17 16 L3 16 Z" fill="#fff"/>
          <circle cx="10" cy="13" r="2" fill="#ff0000"/>
        </svg>
      </span>
    </li>
    <li class="contact__row">
      sales@vantrelle.com.au<br>www.vantrelle.com.au
      <span class="contact__icon">
        <svg viewBox="0 0 20 20" aria-hidden="true">
          <rect x="2" y="3" width="16" height="11" fill="none" stroke="#fff" stroke-width="1.8"/>
          <rect x="8" y="14" width="4" height="2" fill="#fff"/>
          <rect x="5" y="16" width="10" height="1.6" fill="#fff"/>
        </svg>
      </span>
    </li>
    <li class="contact__row">
      Suite xxx, 214 Dawlish Parade<br>Melbourne, Victoria 3000
      <span class="contact__icon">
        <svg viewBox="0 0 20 20" aria-hidden="true">
          <path d="M10 2 L19 10 L16.5 10 L16.5 18 L12 18 L12 13 L8 13 L8 18 L3.5 18 L3.5 10 L1 10 Z" fill="#fff"/>
        </svg>
      </span>
    </li>
  </ul>
</section>

</body>
</html>
```